Need Web Design for Business Process Outsourcing Company (Kelmora)

Kelmora is a business process outsourcing company. Need a simple site similar to http://www.tarvenholm.com/ but with a more professional and credible look. New to the process; not sure where to start and comparing my options. Please let me know what my options are if I choose to go with you. Logo is attached for your reference. Please use same colorway

Reason: I want the final product to be coded. Please confirm you will be able to code final design.

Industry/Entity Type

Business

Coding

Coded - Design and coding required

```html
<!DOCTYPE html>
<html lang="en">
<head>
<meta charset="utf-8">
<title>Kelmora – Business Process Outsourcing</title>
<link href="https://fonts.googleapis.com/css2?family=Open+Sans:wght@400;600;700&display=swap" rel="stylesheet">
<style>
  :root{
    --blue:#1a8ccf;
    --blue-deep:#0f6fae;
    --navy:#0e4d7e;
    --text:#333;
    --muted:#7a7a7a;
    --line:#d9d9d9;
    --soft:#f3f3f3;
    --strip:#f9f9f9;
    --white:#fff;
    --date:#3c3c3c;
  }
  *{box-sizing:border-box;margin:0;padding:0}
  html,body{width:1200px;height:2244px;overflow:hidden}
  body{font-family:"Open Sans",Arial,sans-serif;color:var(--text);background:var(--white);position:relative}
  a{color:inherit;text-decoration:none}

  /* Header */
  .site-header{position:absolute;top:0;left:0;width:1200px;height:112px}
  .brand{position:absolute;left:132px;top:30px;display:flex;align-items:center;gap:10px}
  .brand-mark{width:48px;height:48px;background:var(--blue-deep)}
  .brand-name{font-size:34px;font-weight:700;color:var(--navy);letter-spacing:-0.5px}
  .header-contacts{position:absolute;right:133px;top:38px;display:flex;gap:26px}
  .contact-item{display:flex;align-items:center;gap:6px}
  .contact-text{text-align:right;line-height:1.1}
  .contact-label{font-size:12px;color:var(--text);display:block}
  .contact-value{font-size:19px;color:var(--blue);display:block}
  .contact-icon{width:32px;height:32px;border:1px solid var(--line);border-radius:50%;display:flex;align-items:center;justify-content:center}

  /* Hero */
  .hero{position:absolute;top:112px;left:0;width:1200px;height:505px;overflow:hidden}
  .hero-photo{position:absolute;inset:0;background:
      radial-gradient(ellipse at 30% 45%,#b9c6d2 0%,#8ea6bd 35%,transparent 60%),
      linear-gradient(90deg,#c9d5df 0%,#9fb6cb 40%,#5f7f9e 62%,#2a2f38 80%,#1c1f25 100%)}
  .hero-shape{position:absolute;inset:0}
  .main-nav{position:absolute;top:0;left:0;width:1200px;height:42px;display:flex;justify-content:center;gap:32px;align-items:center}
  .main-nav a{color:var(--white);font-size:12.5px;font-weight:600;text-transform:uppercase}
  .main-nav a.is-active{text-decoration:underline;text-underline-offset:3px}
  .slider-arrow{position:absolute;top:185px;width:25px;height:32px;background:rgba(80,80,80,.55);display:flex;align-items:center;justify-content:center}
  .slider-arrow.prev{left:0}
  .slider-arrow.next{right:0;background:transparent}

  /* Services */
  .services{position:absolute;top:665px;left:132px;width:936px;display:grid;grid-template-columns:repeat(3,1fr);column-gap:0;row-gap:57px}
  .service{text-align:center;width:290px;justify-self:center}
  .service-icon{width:81px;height:81px;border:1px solid #cfcfcf;border-radius:50%;margin:0 auto;display:flex;align-items:center;justify-content:center}
  .service-title{font-size:21px;font-weight:400;color:var(--blue);margin-top:8px;line-height:1.3}
  .service-text{font-size:11px;color:var(--muted);line-height:16px;margin-top:4px}

  /* Promo banner */
  .promo{position:absolute;top:1111px;left:0;width:1200px;height:281px;text-align:center;color:var(--white)}
  .promo-bg{position:absolute;inset:0;background:
      radial-gradient(ellipse at 50% 55%,#2a97d3 0%,#1d86c4 45%,#0e66a3 100%)}
  .promo-content{position:relative;padding-top:76px}
  .promo-title{font-size:30px;font-weight:700}
  .promo-sub{font-size:13px;font-weight:600;margin-top:4px}
  .btn{display:inline-block;font-size:12px;text-transform:uppercase;padding:0;text-align:center}
  .btn-light{background:var(--white);color:#555;width:104px;height:42px;line-height:42px;margin-top:18px}

  /* Projects */
  .projects{position:absolute;top:1460px;left:133px;width:934px}
  .section-title{font-size:21px;font-weight:400;color:var(--blue)}
  .carousel-nav{position:absolute;right:0;top:7px;display:flex;gap:5px}
  .carousel-nav span{width:21px;height:21px;border-radius:50%;background:#e6e6e6;display:flex;align-items:center;justify-content:center}
  .carousel-nav span.on{background:#cfcfcf}
  .project-list{display:flex;gap:20px;margin-top:18px}
  .project{width:298px}
  .project-media{position:relative;height:177px}
  .project-media.hr{background:linear-gradient(120deg,#3f5f85 0%,#6f8fb3 50%,#a7bdd2 100%)}
  .project-media.network{background:linear-gradient(120deg,#c7d0e2 0%,#8fa3c6 45%,#3a4f78 100%)}
  .project-media.support{background:linear-gradient(90deg,#8d959f 0%,#d7d9dc 40%,#eee9e4 75%,#d9cfc5 100%)}
  .date-badge{position:absolute;left:0;bottom:0;width:50px;height:55px;background:var(--date);color:var(--white);text-align:center;padding-top:8px}
  .date-day{font-size:19px;line-height:1.1;display:block}
  .date-month{font-size:9px;display:block}
  .project-title{font-size:17px;color:var(--text);line-height:24px;margin-top:12px;font-weight:400}
  .read-more{font-size:11px;text-decoration:underline;text-transform:uppercase;color:var(--text);display:inline-block;margin-top:8px}

  /* Career */
  .career{position:absolute;top:1843px;left:0;width:1200px;height:239px;background:var(--soft);text-align:center}
  .career .section-title{margin-top:40px}
  .career-text{width:936px;margin:6px auto 0;font-size:12.5px;line-height:21px;color:var(--muted)}
  .btn-dark{background:var(--navy);color:var(--white);width:104px;height:44px;line-height:44px;margin-top:22px}

  /* Contact strip */
  .contact-strip{position:absolute;top:2082px;left:0;width:1200px;height:69px;background:var(--strip);border-top:1px solid #ececec;border-bottom:1px solid #ececec}
  .strip-inner{width:936px;margin:0 auto;height:100%;display:flex;justify-content:space-between;align-items:center;font-size:12px;color:var(--text)}
  .strip-item{display:flex;align-items:center;gap:7px}

  /* Footer */
  .site-footer{position:absolute;top:2151px;left:0;width:1200px;height:93px}
  .footer-inner{width:936px;margin:0 auto;position:relative}
  .footer-links{padding-top:25px;font-size:11px;color:var(--muted)}
  .footer-links a{margin:0 8px}
  .footer-links a:first-child{margin-left:0}
  .copyright{font-size:10.5px;color:var(--muted);margin-top:10px}
  .social{position:absolute;right:0;top:33px;display:flex;gap:7px}
  .social span{width:26px;height:26px;border-radius:50%}
  .s1{background:#3b5998}.s2{background:#1da1f2}.s3{background:#0077b5}.s4{background:#dd4b39}
</style>
</head>
<body>

<header class="site-header">
  <a class="brand" href="#">
    <span class="brand-mark"></span>
    <span class="brand-name">Kelmora</span>
  </a>
  <div class="header-contacts">
    <div class="contact-item">
      <div class="contact-text"><span class="contact-label">Have Questions?</span><span class="contact-value">Live Chat with Us</span></div>
      <span class="contact-icon"><svg width="14" height="13" viewBox="0 0 14 13"><ellipse cx="7" cy="5.5" rx="6.5" ry="5" fill="#999"/><path d="M3 9 L2 12.5 L6 10z" fill="#999"/></svg></span>
    </div>
    <div class="contact-item">
      <div class="contact-text"><span class="contact-label">Email</span><span class="contact-value">info@kelmora.com</span></div>
      <span class="contact-icon"><svg width="14" height="10" viewBox="0 0 14 10"><rect width="14" height="10" rx="1" fill="#999"/><path d="M1 1 L7 6 L13 1" stroke="#fff" stroke-width="1.2" fill="none"/></svg></span>
    </div>
    <div class="contact-item">
      <div class="contact-text"><span class="contact-label">Call us on</span><span class="contact-value">555 201 4470</span></div>
      <span class="contact-icon"><svg width="8" height="14" viewBox="0 0 8 14"><rect x=".6" y=".6" width="6.8" height="12.8" rx="1.2" fill="none" stroke="#888" stroke-width="1.2"/><circle cx="4" cy="11" r=".8" fill="#888"/></svg></span>
    </div>
  </div>
</header>

<section class="hero">
  <div class="hero-photo" role="img" aria-label="Business person touching a network of gears with team member icons and the word team"></div>
  <svg class="hero-shape" width="1200" height="505" viewBox="0 0 1200 505">
    <path d="M0 0 H1200 V30 Q600 58 0 40 Z" fill="#1a8ccf"/>
    <path d="M0 395 Q520 560 1200 450 V505 H0 Z" fill="#fff"/>
  </svg>
  <nav class="main-nav">
    <a class="is-active" href="#">Home</a>
    <a href="#">Who we are</a>
    <a href="#">What we do</a>
    <a href="#">News</a>
    <a href="#">Blog</a>
    <a href="#">Contact Us</a>
  </nav>
  <a class="slider-arrow prev" href="#"><svg width="9" height="16" viewBox="0 0 9 16"><path d="M8 1 L1 8 L8 15" stroke="#fff" stroke-width="1.5" fill="none"/></svg></a>
  <a class="slider-arrow next" href="#"><svg width="9" height="16" viewBox="0 0 9 16"><path d="M1 1 L8 8 L1 15" stroke="#fff" stroke-width="1.5" fill="none"/></svg></a>
</section>

<section class="services">
  <article class="service">
    <div class="service-icon"><svg width="34" height="26" viewBox="0 0 34 26" fill="#1a8ccf"><circle cx="9" cy="7" r="4"/><circle cx="25" cy="7" r="4"/><circle cx="17" cy="9" r="5"/><path d="M2 20c0-5 3-7 7-7s5 2 5 2v5z"/><path d="M32 20c0-5-3-7-7-7s-5 2-5 2v5z"/><path d="M8 26c0-7 4-10 9-10s9 3 9 10z"/></svg></div>
    <h3 class="service-title">Human Resources</h3>
    <p class="service-text">Mauris risus sapien, pharetra dapibus mauris in, hendrerit condimentum sapien. Cras tincidunt in sapien non tempus. Ut iaculis suscipit fermentum. Integer pretium.</p>
  </article>
  <article class="service">
    <div class="service-icon"><svg width="32" height="26" viewBox="0 0 32 26" fill="#1a8ccf"><rect x="12" y="0" width="8" height="7"/><rect x="0" y="19" width="8" height="7"/><rect x="12" y="19" width="8" height="7"/><rect x="24" y="19" width="8" height="7"/><path d="M15.2 7h1.6v5H28v7h-1.6v-5.4h-9.6V19h-1.6v-5.4H5.6V19H4v-7h11.2z"/></svg></div>
    <h3 class="service-title">Project Management</h3>
    <p class="service-text">Mauris risus sapien, pharetra dapibus mauris in, hendrerit condimentum sapien. Cras tincidunt in sapien non tempus. Ut iaculis suscipit fermentum. Integer pretium.</p>
  </article>
  <article class="service">
    <div class="service-icon"><svg width="28" height="28" viewBox="0 0 28 28" fill="#1a8ccf"><path d="M2 8h7a3.5 3.5 0 1 1 7 0h6v7a3.5 3.5 0 1 1 0 7v4H2z"/></svg></div>
    <h3 class="service-title">IT Solutions</h3>
    <p class="service-text">Mauris risus sapien, pharetra dapibus mauris in, hendrerit condimentum sapien. Cras tincidunt in sapien non tempus. Ut iaculis suscipit fermentum. Integer pretium.</p>
  </article>
  <article class="service">
    <div class="service-icon"><svg width="32" height="28" viewBox="0 0 32 28" fill="#1a8ccf"><ellipse cx="16" cy="12" rx="15" ry="11"/><path d="M6 19 L3 27 L13 22z"/></svg></div>
    <h3 class="service-title">Business Consulting</h3>
    <p class="service-text">Mauris risus sapien, pharetra dapibus mauris in, hendrerit condimentum sapien. Cras tincidunt in sapien non tempus. Ut iaculis suscipit fermentum. Integer pretium.</p>
  </article>
  <article class="service">
    <div class="service-icon"><svg width="32" height="28" viewBox="0 0 32 28" fill="#1a8ccf"><rect x="5" y="14" width="4" height="10"/><rect x="11" y="6" width="4" height="18"/><rect x="17" y="10" width="4" height="14"/><rect x="23" y="3" width="4" height="21"/><rect x="1" y="25" width="30" height="2"/><rect x="1" y="1" width="2" height="26"/></svg></div>
    <h3 class="service-title">Trainings</h3>
    <p class="service-text">Mauris risus sapien, pharetra dapibus mauris in, hendrerit condimentum sapien. Cras tincidunt in sapien non tempus. Ut iaculis suscipit fermentum. Integer pretium.</p>
  </article>
  <article class="service">
    <div class="service-icon"><svg width="30" height="30" viewBox="0 0 30 30"><circle cx="15" cy="15" r="11.5" fill="none" stroke="#1a8ccf" stroke-width="5"/><circle cx="15" cy="15" r="11.5" fill="none" stroke="#fff" stroke-width="5.2" stroke-dasharray="4 14.06" stroke-dashoffset="2"/><circle cx="15" cy="15" r="6.5" fill="none" stroke="#1a8ccf" stroke-width="1"/></svg></div>
    <h3 class="service-title">Support</h3>
    <p class="service-text">Mauris risus sapien, pharetra dapibus mauris in, hendrerit condimentum sapien. Cras tincidunt in sapien non tempus. Ut iaculis suscipit fermentum. Integer pretium.</p>
  </article>
</section>

<section class="promo">
  <div class="promo-bg" role="img" aria-label="Business person with a glowing network of people icons in blue"></div>
  <div class="promo-content">
    <h2 class="promo-title">Quisque porta elementum massa eget ultrices</h2>
    <p class="promo-sub">Phasellus urna sapien, lobortis gravida dolor bibendum, varius malesuada odio</p>
    <a class="btn btn-light" href="#">Read more</a>
  </div>
</section>

<section class="projects">
  <h2 class="section-title">Projects</h2>
  <div class="carousel-nav">
    <span><svg width="6" height="9" viewBox="0 0 6 9"><path d="M5 1 L1.5 4.5 L5 8" stroke="#fff" stroke-width="1.5" fill="none"/></svg></span>
    <span class="on"><svg width="6" height="9" viewBox="0 0 6 9"><path d="M1 1 L4.5 4.5 L1 8" stroke="#666" stroke-width="1.5" fill="none"/></svg></span>
  </div>
  <div class="project-list">
    <article class="project">
      <div class="project-media hr" role="img" aria-label="Hand touching a glowing HR interface">
        <div class="date-badge"><span class="date-day">14</span><span class="date-month">NOV</span></div>
      </div>
      <h3 class="project-title">Pellentesque ac orci ut nulla maximus eleifend sed et ligula</h3>
      <a class="read-more" href="#">Read more</a>
    </article>
    <article class="project">
      <div class="project-media network" role="img" aria-label="Hand selecting from a grid of hexagon people icons">
        <div class="date-badge"><span class="date-day">14</span><span class="date-month">NOV</span></div>
      </div>
      <h3 class="project-title">Pellentesque ac orci ut nulla maximus eleifend sed et ligula</h3>
      <a class="read-more" href="#">Read more</a>
    </article>
    <article class="project">
      <div class="project-media support" role="img" aria-label="Customer support agent with a headset">
        <div class="date-badge"><span class="date-day">14</span><span class="date-month">NOV</span></div>
      </div>
      <h3 class="project-title">Pellentesque ac orci ut nulla maximus eleifend sed et ligula</h3>
      <a class="read-more" href="#">Read more</a>
    </article>
  </div>
</section>

<section class="career">
  <h2 class="section-title">Career</h2>
  <p class="career-text">Nullam tristique justo lorem, ut maximus augue scelerisque ut. Duis elementum massa ex, non ultrices leo pellentesque et. Etiam dignissim pulvinar eleifend. Donec convallis faucibus risus nec accumsan. Proin pulvinar erat sed dolor dignissim pulvinar. Nulla sed leo imperdiet, placerat dui non, luctus ex. In et leo nec tortor congue condimentum ac vel arcu. Sed placerat ante a purus placerat vestibulum.</p>
  <a class="btn btn-dark" href="#">Apply now</a>
</section>

<section class="contact-strip">
  <div class="strip-inner">
    <span class="strip-item"><svg width="8" height="12" viewBox="0 0 8 12"><path d="M4 0a4 4 0 0 1 4 4c0 3-4 8-4 8S0 7 0 4a4 4 0 0 1 4-4z" fill="#333"/><circle cx="4" cy="4" r="1.5" fill="#f9f9f9"/></svg>24 Building name, Street name, City - Zipcode</span>
    <span class="strip-item"><svg width="11" height="11" viewBox="0 0 11 11"><path d="M2 0l2 2.5-1.2 1.6a7 7 0 0 0 4.1 4.1L8.5 7 11 9l-1.5 2C4.5 11 0 6.5 0 1.5z" fill="#333"/></svg>555 308 1192</span>
    <span class="strip-item"><svg width="11" height="11" viewBox="0 0 11 11"><rect x="2" y="0" width="7" height="4" fill="#333"/><rect x="0" y="4" width="11" height="7" rx="1" fill="#333"/></svg>Fax : 555 308 1193</span>
    <span class="strip-item"><svg width="12" height="9" viewBox="0 0 12 9"><rect width="12" height="9" rx="1" fill="#333"/><path d="M1 1 L6 5 L11 1" stroke="#f9f9f9" fill="none"/></svg>Email : info@kelmora.com</span>
  </div>
</section>

<footer class="site-footer">
  <div class="footer-inner">
    <nav class="footer-links">
      <a href="#">Home</a>|<a href="#">Who we are</a>|<a href="#">What we do</a>|<a href="#">News</a>|<a href="#">Blog</a>|<a href="#">Contact Us</a>
    </nav>
    <p class="copyright">Copyright © 2016 &nbsp;Company name. &nbsp;All rights reserved.</p>
    <div class="social">
      <span class="s1"></span><span class="s2"></span><span class="s3"></span><span class="s4"></span>
    </div>
  </div>
</footer>

</body>
</html>
```